Realtor branding business card

modern, simple and self branding. Broker office logo needs to be used but not emphasized. Looking to brand myself

Target Market(s)

buyers, sellers and investors

Industry/Entity Type

Realtor

Contact Information for Business Card

Sample of my current business card on file

Requirements
Must have
• my website - emilioverdaskt.com
• Realtor logo
• Fair housing logo
Nice to have
• Colors from office logo but not a must
Should not have
• Do not want headshot

```html
<!DOCTYPE html>
<html lang="en">
<head>
<meta charset="utf-8">
<title>Emilio Verdask – Realtor Business Card</title>
<link href="https://fonts.googleapis.com/css2?family=Oswald:wght@500;700&family=Lato:wght@400;700&display=swap" rel="stylesheet">
<style>
  :root {
    --canvas: #ecebef;
    --indigo: #3d3880;
    --indigo-deep: #2b2768;
    --navy-ink: #27236b;
    --accent-red: #c8242b;
    --skyline: #dddce8;
    --paper: #ffffff;
    --text-light: #f2f1f8;
  }
  * { box-sizing: border-box; margin: 0; padding: 0; }
  html, body {
    width: 1200px; height: 1200px; overflow: hidden;
    background: var(--canvas);
  }
  .sheet {
    width: 1200px; height: 1200px;
    display: flex; flex-direction: column; align-items: center; justify-content: center;
    gap: 40px;
  }
  .card {
    width: 920px; height: 526px;
    border-radius: 4px;
    overflow: hidden;
    box-shadow: 0 6px 18px rgba(30, 28, 70, 0.18);
    position: relative;
  }

  /* Back */
  .card-back {
    background: linear-gradient(135deg, var(--indigo-deep) 0%, var(--indigo) 60%, #5a5696 100%);
    display: flex; align-items: center; justify-content: center;
  }
  .brand-mark {
    display: flex; align-items: center; gap: 18px;
    font-family: "Oswald", sans-serif; font-weight: 700;
    color: var(--paper);
    font-size: 64px; line-height: 1; letter-spacing: 1px;
    text-transform: uppercase;
  }
  .brand-mark .brand-square {
    width: 34px; height: 34px; background: currentColor; flex: none;
  }

  /* Front */
  .card-front { display: flex; }
  .front-brand {
    width: 44%; background: var(--paper); position: relative;
  }
  .skyline {
    position: absolute; left: 0; right: 0; bottom: 0; height: 52%;
    background: linear-gradient(180deg, #e6e5ee 0%, var(--skyline) 100%);
  }
  .front-brand .brand-mark {
    position: absolute; left: 34px; right: 28px; top: 150px;
    color: var(--navy-ink);
    font-size: 44px; line-height: 1.05; flex-wrap: wrap; gap: 10px 12px;
  }
  .front-brand .brand-mark .brand-square {
    width: 26px; height: 26px; background: var(--accent-red);
  }
  .front-contact {
    flex: 1;
    background: linear-gradient(160deg, var(--indigo) 0%, var(--indigo-deep) 100%);
    color: var(--text-light);
    padding: 112px 36px 0 44px;
    font-family: "Lato", sans-serif;
  }
  .agent-name {
    font-family: "Oswald", sans-serif; font-weight: 500;
    font-size: 44px; letter-spacing: 1px; text-transform: uppercase;
    color: var(--paper); line-height: 1.1;
  }
  .agent-title {
    color: var(--accent-red); font-size: 26px; margin-bottom: 14px;
  }
  .contact-list { list-style: none; }
  .contact-list li {
    display: flex; align-items: center; gap: 14px;
    font-size: 22px; line-height: 1.45; letter-spacing: 0.3px;
    white-space: nowrap;
  }
  .contact-list svg { width: 18px; height: 18px; flex: none; fill: var(--accent-red); }
  .contact-list .label { width: 78px; }
  .address { font-size: 22px; line-height: 1.4; margin-top: 8px; letter-spacing: 0.3px; }
  .badges { display: flex; gap: 10px; margin-top: 20px; }
  .badge { width: 36px; height: 36px; border: 3px solid var(--paper); }
  .badge-house { border-radius: 50%; }
</style>
</head>
<body>
<main class="sheet">
  <section class="card card-back">
    <div class="brand-mark"><span class="brand-square"></span>Keystone Hearth Realty</div>
  </section>

  <section class="card card-front">
    <div class="front-brand">
      <div class="skyline" role="img" aria-label="Light grey city skyline illustration of tall buildings"></div>
      <div class="brand-mark"><span class="brand-square"></span>Keystone Hearth Realty</div>
    </div>
    <div class="front-contact">
      <h1 class="agent-name">Emilio Verdask</h1>
      <p class="agent-title">Realtor</p>
      <ul class="contact-list">
        <li>
          <svg viewBox="0 0 24 24"><path d="M6.6 10.8a15 15 0 0 0 6.6 6.6l2.2-2.2a1 1 0 0 1 1-.25 11.4 11.4 0 0 0 3.6.57 1 1 0 0 1 1 1V20a1 1 0 0 1-1 1A17 17 0 0 1 3 4a1 1 0 0 1 1-1h3.5a1 1 0 0 1 1 1c0 1.250.2 2.450.57 3.570a1 1 0 0 1-.25 1z"/></svg>
          <span class="label">Cell:</span><span>+407 - 555 - 0148</span>
        </li>
        <li>
          <svg viewBox="0 0 24 24"><path d="M2 9c4-4 16-4 20 0l-3 3-3-2V8H8v2l-3 2zM6 13h12l2 7H4z"/></svg>
          <span class="label">Office:</span><span>+407 - 555 - 0192</span>
        </li>
        <li>
          <svg viewBox="0 0 24 24"><path d="M2 5h20v14H2zm2 2v.5l8 5 8-5V7z"/></svg>
          <span>everdask@emilioverdaskt.com</span>
        </li>
        <li>
          <svg viewBox="0 0 24 24"><path d="M12 2a10 10 0 1 0 0 20 10 10 0 0 0 0-20zm0 2c1.2 1.5 2 3.5 2.2 6H9.8C10 7.5 10.8 5.5 12 4zm-2.2 8h4.4c-.2 2.5-1 4.5-2.2 6-1.2-1.5-2-3.5-2.2-6zM4.1 12h3.7c.1 2 .6 3.9 1.4 5.4A8 8 0 0 1 4.1 12zm0-2a8 8 0 0 1 5.1-5.4C8.4 6.1 7.9 8 7.8 10zm12.1 0c-.1-2-.6-3.9-1.4-5.4a8 8 0 0 1 5.1 5.4zm0 2h3.7a8 8 0 0 1-5.1 5.4c.8-1.5 1.3-3.4 1.4-5.4z"/></svg>
          <span>www.emilioverdaskt.com</span>
        </li>
      </ul>
      <p class="address">48 North Cedar Ridge<br>Dr. Lakewood Springs, FL 32790</p>
      <div class="badges">
        <span class="badge"></span>
        <span class="badge badge-house"></span>
      </div>
    </div>
  </section>
</main>
</body>
</html>
```